Kalmoret Windham & Associates

We would like a simple, professional business card using a similar font to our logo.

Industry/Entity Type

Law Firm

Contact Information for Business Card

Martin Kalmoret, Esq. 47 Tillman Lane, 2nd Floor Brantwell, MA 02091 Office: 781.555.0143 Cell: 508.555.0196 Email: marty@kwfirmma.com kalmoretwindhamlaw.com

Font styles to use
Other font styles liked:
• We would like to use the fonts used in the logo or similar

Colors
0054AA
0677BA
7BADD7
CADEEF
E8F1F8

Requirements
Must have
• We would like the fonts to match the logo
Nice to have
• not too much design- very simple and professional business card. I added a picture of a business card that I tried to start but I am not a designer! Hopefully it will help with the address and phone numbers and kind of what we are looking for.

```html
<!DOCTYPE html>
<html lang="en">
<head>
<meta charset="utf-8">
<title>Kalmoret Windham &amp; Associates – Business Card</title>
<link href="https://fonts.googleapis.com/css2?family=Cinzel:wght@500;600&family=Poppins:wght@300;400&display=swap" rel="stylesheet">
<style>
  :root {
    --bg: #222222;
    --brand-blue: #0054aa;
    --brand-blue-light: #0677ba;
    --navy: #1f3c8c;
    --paper: #f1f2f4;
    --ink-grey: #6b6f76;
    --rule: #3d5aa6;
    --white: #ffffff;
  }
  * { box-sizing: border-box; margin: 0; padding: 0; }
  html, body { width: 1200px; height: 824px; overflow: hidden; }
  body {
    background: var(--bg);
    display: flex;
    flex-direction: column;
    align-items: center;
    justify-content: center;
    gap: 40px;
  }
  .card {
    width: 560px;
    height: 320px;
    position: relative;
    box-shadow: 0 14px 30px rgba(0,0,0,.45);
  }

  /* Front */
  .card-front {
    background: linear-gradient(135deg, var(--brand-blue-light) 0%, var(--brand-blue) 55%, #0a4fa3 100%);
    display: flex;
    align-items: center;
    justify-content: center;
  }
  .front-name {
    font-family: "Cinzel", serif;
    font-weight: 600;
    color: var(--white);
    font-size: 30px;
    line-height: 1.25;
    letter-spacing: 2px;
    text-align: center;
  }

  /* Back */
  .card-back { background: var(--paper); }
  .firm {
    position: absolute;
    left: 36px;
    top: 34px;
    display: flex;
    align-items: center;
    gap: 12px;
  }
  .firm-square {
    width: 58px;
    height: 58px;
    background: var(--navy);
  }
  .firm-divider {
    width: 1px;
    height: 62px;
    background: var(--ink-grey);
  }
  .firm-name {
    font-family: "Cinzel", serif;
    font-weight: 600;
    color: var(--navy);
    font-size: 15px;
    line-height: 1.05;
    letter-spacing: .5px;
  }
  .person {
    position: absolute;
    right: 34px;
    top: 112px;
    text-align: right;
  }
  .person-name {
    font-family: "Cinzel", serif;
    font-weight: 600;
    color: var(--navy);
    font-size: 24px;
    letter-spacing: 1px;
    line-height: 1;
  }
  .person-title {
    font-family: "Poppins", sans-serif;
    font-weight: 300;
    color: var(--ink-grey);
    font-size: 14px;
    margin-top: 2px;
  }
  .divider-rule {
    position: absolute;
    left: 34px;
    right: 28px;
    top: 178px;
    height: 1px;
    background: var(--rule);
  }
  .contact {
    position: absolute;
    left: 40px;
    top: 196px;
    list-style: none;
    font-family: "Poppins", sans-serif;
    font-weight: 300;
    font-size: 10.5px;
    color: var(--ink-grey);
  }
  .contact li {
    display: flex;
    align-items: center;
    gap: 12px;
    height: 19px;
  }
  .contact svg { width: 12px; height: 12px; fill: none; stroke: var(--navy); stroke-width: 1.6; }
  .address {
    position: absolute;
    right: 34px;
    top: 196px;
    text-align: right;
    font-family: "Poppins", sans-serif;
    font-weight: 300;
    font-style: normal;
    font-size: 9.5px;
    line-height: 1.45;
    color: var(--ink-grey);
  }
</style>
</head>
<body>

<section class="card card-front">
  <p class="front-name">Kalmoret Windham<br>&amp; Associates</p>
</section>

<section class="card card-back">
  <div class="firm">
    <div class="firm-square"></div>
    <div class="firm-divider"></div>
    <p class="firm-name">Kalmoret<br>Windham<br>&amp; Associates</p>
  </div>

  <div class="person">
    <p class="person-name">Martin Kalmoret</p>
    <p class="person-title">Esquire</p>
  </div>

  <div class="divider-rule"></div>

  <ul class="contact">
    <li>
      <svg viewBox="0 0 12 12"><path d="M2.5 1.5 L4.5 1.5 L5.2 4 L4 5 Q5 7.2 7 8 L8 6.8 L10.5 7.5 L10.5 9.5 Q6 10.5 3 7.5 Q1 5 2.5 1.5 Z"/></svg>
      <span>781.555.0143</span>
    </li>
    <li>
      <svg viewBox="0 0 12 12"><rect x="3" y="1" width="6" height="10" rx="1"/><line x1="5.5" y1="9.2" x2="6.5" y2="9.2"/></svg>
      <span>508.555.0196</span>
    </li>
    <li>
      <svg viewBox="0 0 12 12"><rect x="1" y="2.5" width="10" height="7"/><path d="M1 2.5 L6 6.5 L11 2.5"/></svg>
      <span>marty@kwfirmma.com</span>
    </li>
    <li>
      <svg viewBox="0 0 12 12"><circle cx="6" cy="6" r="5"/><ellipse cx="6" cy="6" rx="2.2" ry="5"/><line x1="1" y1="6" x2="11" y2="6"/></svg>
      <span>kalmoretwindhamlaw.com</span>
    </li>
  </ul>

  <address class="address">
    47 Tillman Lane,<br>
    2nd Floor Brantwell,<br>
    MA 02091.
  </address>
</section>

</body>
</html>
```